Design an Outstanding flyer for my company.

I need a flyer designed for our window tinting company based in Brisbane Queensland Australia. The flyer will be targeting Home tinting. We also do mobile car tinting. Something in regards to this could be incorporated into the flyer as well.
I want it to be 2 sided DL size. Black background.
It really needs to Pop, and be a real attention getter.
It needs to be easy to read.
I have provided a mock up with the info on it from our marketing company. It will need a spellcheck etc to make sure everything is correct.
Everything about it can be changed however you like.
I have also included the company logo.

Lets see what you've got!

Target Market(s)

Home Owners

Industry/Entity Type

Home Improvement

Font styles to use
Other font styles liked:
• Duan Penh

Requirements
Must have
• All the information on the mock up. Clear and easy to read.
• Must Stand Out!

```html
<!DOCTYPE html>
<html lang="en">
<head>
<meta charset="utf-8">
<title>BrightLine Window Tinting – DL Flyer</title>
<link href="https://fonts.googleapis.com/css2?family=Marcellus&family=Cinzel:wght@400;700&display=swap" rel="stylesheet">
<style>
  :root {
    --page-bg: #e8e5e1;
    --flyer-dark: #111111;
    --flyer-mid: #2c2c2c;
    --gold: #f6c500;
    --gold-light: #ffe34a;
    --gold-deep: #e0a800;
    --ink: #1a1a1a;
    --white: #ffffff;
    --body-text: #d8d8d8;
  }
  * { margin: 0; padding: 0; box-sizing: border-box; }
  html, body { width: 1200px; height: 1000px; overflow: hidden; background: var(--page-bg); }
  .canvas { position: relative; width: 1200px; height: 1000px; }

  .flyer {
    position: absolute; top: 38px; width: 431px; height: 915px;
    background: radial-gradient(ellipse at 50% 45%, var(--flyer-mid) 0%, var(--flyer-dark) 70%);
    box-shadow: 0 4px 14px rgba(0,0,0,.35);
    color: var(--white);
    overflow: hidden;
  }
  .flyer--front { left: 112px; }
  .flyer--back { left: 620px; }

  .headline-stack {
    position: absolute; left: 30px; width: 371px;
    font-family: "Marcellus", serif; text-align: center;
  }
  .flyer--front .headline-stack { top: 37px; }
  .flyer--back .headline-stack { top: 172px; }
  .headline-stack .line { display: block; white-space: nowrap; }
  .headline-stack .rule { display: block; height: 2px; background: var(--gold); }
  .line--heat { font-size: 43px; line-height: 44px; color: var(--white); letter-spacing: .5px; }
  .line--uv { font-size: 32px; line-height: 38px; color: var(--gold); }
  .line--money { font-size: 50px; line-height: 52px; color: var(--gold); background: linear-gradient(var(--gold-light), var(--gold-deep)); -webkit-background-clip: text; background-clip: text; -webkit-text-fill-color: transparent; }
  .line--privacy { font-size: 36px; line-height: 42px; color: var(--white); }

  .benefits {
    position: absolute; left: 34px; width: 363px;
    font-family: "Cinzel", serif; font-size: 10px; line-height: 18px;
    color: var(--body-text); text-align: center; text-transform: uppercase;
  }
  .flyer--front .benefits { top: 252px; }
  .flyer--back .benefits { top: 396px; }

  .reasons-box {
    position: absolute; left: 48px; width: 335px; height: 97px;
    background: linear-gradient(var(--gold-light), var(--gold) 55%, var(--gold-deep));
    border-radius: 7px; padding: 4px;
  }
  .flyer--front .reasons-box { top: 430px; }
  .flyer--back .reasons-box { top: 42px; }
  .reasons-box__inner {
    width: 100%; height: 100%; border: 1.5px dotted rgba(60,40,0,.55); border-radius: 5px;
    display: flex; align-items: center; justify-content: center; text-align: center;
    font-family: "Cinzel", serif; font-weight: 700; font-size: 20px; line-height: 24px; color: var(--ink);
  }

  .call-band { position: absolute; left: 0; width: 431px; height: 82px; }
  .flyer--front .call-band { top: 564px; }
  .flyer--back .call-band { top: 567px; }
  .call-band svg { position: absolute; inset: 0; }
  .call-band__text {
    position: absolute; inset: 0; display: flex; align-items: center; justify-content: center;
    text-align: center; font-family: "Marcellus", serif; font-size: 21px; line-height: 22px; color: var(--ink);
  }

  .contact-list { position: absolute; top: 664px; left: 0; width: 431px; font-family: "Marcellus", serif; font-size: 27px; }
  .contact-list li { list-style: none; display: flex; align-items: center; justify-content: center; height: 35px; gap: 8px; }
  .contact-list svg { width: 20px; height: 20px; }

  .brand { position: absolute; top: 782px; left: 0; width: 431px; height: 50px; display: flex; align-items: center; justify-content: center; gap: 12px; }
  .brand__dot { flex: none; width: 30px; height: 30px; border-radius: 50%; background: var(--gold); }
  .brand__name { font-family: "Marcellus", serif; font-size: 24px; color: var(--gold); white-space: nowrap; }

  .web-pill {
    position: absolute; top: 859px; left: 108px; width: 215px; height: 24px;
    background: var(--gold); border-radius: 4px; color: var(--ink);
    font-family: "Marcellus", serif; font-size: 13.5px;
    display: flex; align-items: center; justify-content: center;
  }
</style>
</head>
<body>
<div class="canvas">

  <section class="flyer flyer--front">
    <div class="headline-stack">
      <span class="line line--heat">KEEP HEAT OUT</span>
      <span class="rule"></span>
      <span class="line line--uv">BLOCK 99.9% UV RAYS</span>
      <span class="rule"></span>
      <span class="line line--money">SAVE MONEY</span>
      <span class="rule"></span>
      <span class="line line--privacy">INCREASE PRIVACY</span>
    </div>
    <p class="benefits">Reduce glare. Reduce energy costs. Control the amount of light entering your home. Reduce carbon footprint. Make home more beautiful. Eliminate home hot spots. Protect against broken glass. Regulate energy. Protects upholstery. Improve effectiveness of roof insulation. Improve health. Reduces interior floor fading. Eliminate need for blinds. Strengthen your windows. Insulate in winter. Affordable.</p>
    <div class="reasons-box"><div class="reasons-box__inner">20 REASONS WHY<br>HOME WINDOW TINTING<br>IS PERFECT FOR YOU.</div></div>
    <div class="call-band">
      <svg viewBox="0 0 431 82" preserveAspectRatio="none"><defs><linearGradient id="bandFront" x1="0" y1="0" x2="0" y2="1"><stop offset="0" stop-color="#ffe04a"/><stop offset="1" stop-color="#e8b000"/></linearGradient></defs><polygon points="0,0 215,22 431,0 431,82 215,62 0,82" fill="url(#bandFront)"/></svg>
      <div class="call-band__text">CALL BRISBANE’S LEADER IN<br>HOME WINDOW TINTING NOW.</div>
    </div>
    <ul class="contact-list">
      <li><svg viewBox="0 0 20 20"><circle cx="10" cy="10" r="8.5" fill="none" stroke="#f6c500" stroke-width="2"/><path d="M7 6l2 2-1 1.5c.6 1.2 1.3 1.9 2.5 2.5L12 11l2 2-1.3 1.3C9.5 14 6 10.5 5.7 7.3z" fill="#f6c500"/></svg>07 3184 5520</li>
      <li><svg viewBox="0 0 20 20"><rect x="4" y="2" width="9" height="16" rx="1.5" fill="#f6c500"/><rect x="9" y="5" width="9" height="6" rx="1" fill="#f6c500" stroke="#111" stroke-width="1"/></svg>0400 582 936</li>
    </ul>
    <div class="brand"><span class="brand__dot"></span><span class="brand__name">BRIGHTLINE WINDOW TINTING</span></div>
    <div class="web-pill">www.brightlinetinting.com.au</div>
  </section>

  <section class="flyer flyer--back">
    <div class="reasons-box"><div class="reasons-box__inner">20 REASONS WHY<br>HOME WINDOW TINTING<br>IS PERFECT FOR YOU.</div></div>
    <div class="headline-stack">
      <span class="line line--heat">KEEP HEAT OUT</span>
      <span class="rule"></span>
      <span class="line line--uv">BLOCK 99.9% UV RAYS</span>
      <span class="rule"></span>
      <span class="line line--money">SAVE MONEY</span>
      <span class="rule"></span>
      <span class="line line--privacy">INCREASE PRIVACY</span>
    </div>
    <p class="benefits">Reduce glare. Reduce energy costs. Control the amount of light entering your home. Reduce carbon footprint. Make home more beautiful. Eliminate home hot spots. Protect against broken glass. Regulate energy. Protects upholstery. Improve effectiveness of roof insulation. Improve health. Reduces interior floor fading. Eliminate need for blinds. Strengthen your windows. Insulate in winter. Affordable.</p>
    <div class="call-band">
      <svg viewBox="0 0 431 82" preserveAspectRatio="none"><defs><linearGradient id="bandBack" x1="0" y1="0" x2="0" y2="1"><stop offset="0" stop-color="#ffe04a"/><stop offset="1" stop-color="#e8b000"/></linearGradient></defs><polygon points="0,0 215,22 431,0 431,82 215,62 0,82" fill="url(#bandBack)"/></svg>
      <div class="call-band__text">CALL BRISBANE’S LEADER IN<br>HOME WINDOW TINTING NOW.</div>
    </div>
    <ul class="contact-list">
      <li><svg viewBox="0 0 20 20"><circle cx="10" cy="10" r="8.5" fill="none" stroke="#f6c500" stroke-width="2"/><path d="M7 6l2 2-1 1.5c.6 1.2 1.3 1.9 2.5 2.5L12 11l2 2-1.3 1.3C9.5 14 6 10.5 5.7 7.3z" fill="#f6c500"/></svg>07 3184 5520</li>
      <li><svg viewBox="0 0 20 20"><rect x="4" y="2" width="9" height="16" rx="1.5" fill="#f6c500"/><rect x="9" y="5" width="9" height="6" rx="1" fill="#f6c500" stroke="#111" stroke-width="1"/></svg>0400 582 936</li>
    </ul>
    <div class="brand"><span class="brand__dot"></span><span class="brand__name">BRIGHTLINE WINDOW TINTING</span></div>
    <div class="web-pill">www.brightlinetinting.com.au</div>
  </section>

</div>
</body>
</html>
```